Morrowbrook Services Destination Map

We need a graphic representation of the ideas in the attached word document.
The destination is the same – the Highest Quality of Care for you or your aging loved one.
How we sell ourselves as a valuable partner/guide on the aging life care journey:
Other things to consider when deciding if you want Morrowbrook Services to help you on your journey:
• We can do in 2 hours what it would take you 2 weeks to do.
• We’re much cheaper that the cost of plan fare if you have to fly into town when your father has that next car crash.
• We can tell you which nursing home or assisted living community you don’t want to visit.
• We can make your parents hear what you have said over and over again, but they refuse to listen because you are still a child.
• We have helped hundreds of seniors a lot worse than yours.
• We’re available 24/7, so you can turn your phone off.
Target Market(s)
Senior Care Market
Adult Children of seniors who have become the primary caregiver for their aging parent

```html
<!DOCTYPE html>
<html lang="en">
<head>
<meta charset="utf-8">
<title>Morrowbrook Services – Destination Map</title>
<link rel="stylesheet" href="https://fonts.googleapis.com/css2?family=Raleway:wght@300;400;500&family=Nunito:wght@800;900&display=swap">
<style>
  :root{
    --ink:#565656;
    --teal-deep:#2c7487;
    --teal-mid:#3a8b97;
    --teal-soft:#8fd6cf;
    --teal-band:#6dbdb8;
    --teal-head:#3e9b9c;
    --slate:#5b6e92;
    --footer:#2e7886;
    --white:#ffffff;
    --photo-warm:#b9a58f;
  }
  *{box-sizing:border-box;margin:0;padding:0}
  html,body{width:848px;height:1200px;overflow:hidden;background:var(--white)}
  .sheet{position:relative;width:848px;height:1200px;font-family:"Raleway",sans-serif;color:var(--ink)}
  .hero-photo{position:absolute;left:0;top:0;width:410px;height:272px;
    background:linear-gradient(135deg,#d8c7a8 0%,var(--photo-warm) 45%,#7c6a5a 100%)}
  .intro{position:absolute;left:410px;top:0;width:438px;height:312px;
    background:linear-gradient(180deg,var(--teal-mid),var(--teal-deep));
    padding:12px 8px 0 20px;font-size:18.8px;line-height:24px;color:var(--white);font-weight:400}
  .intro .soft{color:var(--teal-soft)}
  .accent-bar{position:absolute;left:410px;top:326px;width:438px;height:21px;
    background:linear-gradient(90deg,#6cbcb6,var(--teal-deep) 55%,var(--slate))}
  .brand{position:absolute;left:60px;top:292px;display:flex;align-items:center;gap:22px}
  .brand-mark{width:82px;height:82px;background:var(--teal-head)}
  .brand-name{font-family:"Raleway",sans-serif;font-weight:500;font-size:38px;line-height:40px;color:var(--slate)}
  .formula{position:absolute;left:28px;top:408px;font-size:38.5px;font-weight:300;color:var(--ink);white-space:nowrap}
  .col{position:absolute;top:498px;font-size:18.6px;line-height:22.2px;font-weight:400}
  .col h2{font-family:"Nunito",sans-serif;font-weight:900;font-size:20px;line-height:26px;color:var(--teal-head);margin-bottom:4px}
  .about{left:28px;width:384px}
  .services{left:443px;width:402px}
  .divider{position:absolute;left:422px;top:520px;width:3px;height:336px;background:var(--teal-deep)}
  .equation{display:grid;grid-template-columns:107px 38px auto;margin-top:22px}
  .stops{position:absolute;left:0;top:893px;width:848px;height:242px;background:var(--teal-band)}
  .stops h2{position:absolute;left:30px;top:10px;font-family:"Nunito",sans-serif;font-weight:900;font-size:21.5px;color:var(--white)}
  .stops ul{position:absolute;top:42px;list-style:none;color:var(--white);font-size:16px;line-height:20.5px;font-weight:400}
  .stops .c1{left:21px}.stops .c2{left:284px}.stops .c3{left:445px}
  .stops-photo{position:absolute;left:560px;top:893px;width:288px;height:242px;
    background:linear-gradient(120deg,rgba(109,189,184,0) 0%,#b89a80 30%,#4aa7a6 60%,#5b3f70 100%)}
  .stops-overlay{background:transparent;pointer-events:none}
  .footer{position:absolute;left:0;top:1143px;width:848px;height:57px;background:var(--footer);
    display:flex;align-items:center;justify-content:center;
    font-family:"Nunito",sans-serif;font-weight:800;font-size:23px;color:var(--white)}
</style>
</head>
<body>
<div class="sheet">
  <div class="hero-photo" role="img" aria-label="Care manager meeting with a senior and her family at a table, reviewing documents"></div>

  <div class="intro">
    It is a <span class="soft">journey</span> that no one is ready for and most never plan for. <span class="soft">Each journey is different</span> depending on physical health, mental health, financial resources, family support, experience and additional responsibilities.<span class="soft">The primary caregiver</span> is typically trying to make decisions <span class="soft">under stress and is frustrated</span> from dealing with <span class="soft">too many options and not enough time</span> to figure out what are the best options – <span class="soft">or which stops to make depending on individual needs.</span>
  </div>
  <div class="accent-bar"></div>

  <div class="brand">
    <div class="brand-mark"></div>
    <div class="brand-name">Morrowbrook<br>Services</div>
  </div>

  <h1 class="formula">Education + Training + Experience = Expertise</h1>

  <section class="col about">
    <h2>About us:</h2>
    <p>We know these roads because we have been the guides for families like yours since 1989.</p>
    <p>Don’t Worry, We Know The Way:Our Care Managers have the Education, Training and Experience to help guide you to the stops you need to make in your personal Aging Life Care Journey.</p>
    <p>What our Care Managers have that gives us the Expertise to be the guides towards the main destination:</p>
    <div class="equation">
      <span>Education<br>Training<br>Experience</span>
      <span><br>+</span>
      <span><br>= Expertise</span>
    </div>
  </section>

  <div class="divider"></div>

  <section class="col services">
    <h2>Services:</h2>
    <p>• We can do in 2 hours what it would take you 2 weeks to do.</p>
    <p>• We’re much cheaper that the cost of plan fare if you have to fly into town<br>when your father has that next car crash.</p>
    <p>• We can tell you which nursing home or assisted living community you don’t want to visit.</p>
    <p>• We can make your parents hear what you have said over and over again,<br>but they refuse to listen because you are still a child.</p>
    <p>• We have helped hundreds of seniors a lot worse than yours.</p>
    <p>• We’re available 24/7, so you can turn your phone off.</p>
  </section>

  <section class="stops">
    <h2>List of Aging Care Stops along the journey:</h2>
    <ul class="c1">
      <li>Assisted Living</li><li>Non-Medical In-Home Care</li><li>Primary Care Physician</li>
      <li>Nursing Home</li><li>Pharmacy</li><li>Elder Law Attorney</li>
      <li>Financial Planner</li><li>Conservator</li><li>Local Senior Care Resources</li>
    </ul>
    <ul class="c2">
      <li>Senior Center</li><li>Home Safety</li><li>Home Health</li>
      <li>Hospital</li><li>Hospice</li><li>Board &amp; Care</li>
      <li>Medical Equipment</li><li>Estate Planner</li><li>Fiduciary</li>
    </ul>
  </section>
  <div class="stops-photo" role="img" aria-label="Younger woman and senior woman looking through a photo album together on a sofa"></div>
  <section class="stops stops-overlay">
    <ul class="c3">
      <li>Government Programs</li><li>Medicare, Long</li><li>Villages Network</li>
      <li>Independent Living</li><li>Dementia Care</li>
    </ul>
  </section>

  <footer class="footer">www.morrowbrookanswers.com</footer>
</div>
</body>
</html>
```